Flyer/Poster to promote Bicycle Race

We need a flyer that promotes a bicycle race in downtown Denver. It need to inspire spectators to come watch and bicycle racers to come race. It benefits the Tall Pines Cycling Club is getting urban kids on bikes; sharing healthy lifestyle and values
. We want the colors to be the colors of the logo - blue & red. Community Partnerships must have their logos on the flyer. Flyer must be able to be printed in 8 1/2 x 11 and 11 x 17

Target Market(s)

Neighborhood residents, athletes, cyclists

Industry/Entity Type

Non Profit

Font styles to use
Serif
Sans Serif

Colors
0592cd
ec1f27

Requirements
Must have
• Sunday, July 31, 2016
• Schedule:
• • Racing starts at 7:00am
• • Fun Ride on the Race Course at 12pm
• • Expo & Festival 10am – 6pm
• A Bike Race for Amateurs and Professionals
• A Bike Race for the young, the old & everyone in the middle.
• Great for spectators. Hang out, watch the action & explore the Festival
• Grab a bite to eat & cheer on the racers as they fly around the corners
• Special activities for kids: Wobblo Course, Maple the Moose & More!!
• Renaldo Vasquez Pinefield Radio Music Director and Crosstown Groove Hour host will be onsite!
• Start/Finish/Festival will be on Larkwell St between 9th Ave & 11th Ave
• Net proceeds benefit the Tall Pines Cycling Club dedicated to getting urban youth on bikes; sharing healthy lifestyle and values
• Special thanks to the Harrowgate Foundation for their ongoing support
• LARKWELLSTCRIT.COM

```html
<!DOCTYPE html>
<html lang="en">
<head>
<meta charset="utf-8">
<title>Denver Bicycle Festival</title>
<link href="https://fonts.googleapis.com/css2?family=Montserrat:wght@500;600;700;800&display=swap" rel="stylesheet">
<style>
  :root {
    --blue: #4a8fd8;
    --blue-deep: #3f7fcf;
    --red: #d3111c;
    --ink: #1c1c1c;
    --white: #ffffff;
  }
  html, body { margin: 0; padding: 0; overflow: hidden; background: var(--white); }
  .poster {
    position: relative; width: 927px; height: 1200px; overflow: hidden;
    background: var(--white); font-family: "Montserrat", Arial, sans-serif; color: var(--ink);
  }
  .hero-photo {
    position: absolute; left: 0; top: 140px; width: 927px; height: 650px;
    background: linear-gradient(120deg, #3e5a2c 0%, #6d8a4a 30%, #8c2b2b 55%, #c93b3b 70%, #2b2b2b 85%, #6f8f4c 100%);
  }
  .frame { position: absolute; left: 0; top: 0; width: 927px; height: 1200px; }
  .site-url {
    position: absolute; top: 22px; left: 0; width: 927px; text-align: center;
    font-weight: 700; font-size: 14px; letter-spacing: 2px; color: var(--white);
  }
  .event-title {
    position: absolute; top: 74px; left: 0; width: 927px; margin: 0; text-align: center;
    font-weight: 800; font-size: 39px; line-height: 48px; color: var(--white);
  }
  .event-date {
    position: absolute; top: 738px; left: 27px; margin: 0;
    font-weight: 800; font-size: 42px; line-height: 52px; color: var(--white); white-space: nowrap;
  }
  .details {
    position: absolute; left: 29px; top: 843px; width: 625px;
    font-size: 16px; line-height: 22px; font-weight: 500; margin: 0;
  }
  .schedule {
    position: absolute; left: 659px; top: 836px; width: 226px; height: 203px;
    box-sizing: border-box; padding: 22px 14px; background: var(--blue);
    color: var(--white); font-size: 15.5px; line-height: 21.5px; text-transform: uppercase;
  }
  .schedule h2 { margin: 0 0 14px; font-size: 19px; font-weight: 800; }
  .schedule p { margin: 0; font-weight: 600; }
  .partners {
    position: absolute; left: 18px; top: 1126px; width: 895px; height: 66px;
    display: flex; justify-content: space-between; align-items: center;
  }
  .partner {
    display: flex; align-items: center; gap: 6px;
    font-weight: 700; font-size: 14px; line-height: 1.1;
  }
  .mark { width: 18px; height: 18px; flex: none; }
  .badge { width: 58px; height: 58px; background: var(--red); border-radius: 4px; }
</style>
</head>
<body>
<div class="poster">
  <div class="hero-photo" role="img" aria-label="Photo of a pack of road racers in red and black kits riding in a line through a corner"></div>

  <svg class="frame" viewBox="0 0 927 1200" aria-hidden="true">
    <polygon points="0,0 927,0 927,145 530,145 463,182 396,145 0,145" fill="var(--blue)"/>
    <polygon points="555,792 927,470 927,792" fill="var(--blue-deep)"/>
    <polygon points="585,792 927,495 927,792" fill="var(--white)"/>
    <rect x="0" y="790" width="927" height="410" fill="var(--white)"/>
    <polygon points="0,712 575,712 545,792 0,792" fill="var(--red)"/>
  </svg>

  <div class="site-url">WWW.LARKWELLSTCRIT.COM</div>
  <h1 class="event-title">DENVER BICYCLE FESTIVAL</h1>
  <h2 class="event-date">SUNDAY, JULY 31, 2016</h2>

  <p class="details">
    A Bike Race for Amateurs and Professionals.<br>
    A Bike Race for the young, the old &amp; everyone in the middle.<br>
    Great for spectators. Hang out, watch the action &amp; explore the Festival.<br>
    Grab a bite to eat &amp; cheer on the racers as they fly around the corners.<br>
    Special activities for kids: Wobblo Course, Maple the Moose &amp; More!!<br>
    Renaldo Vasquez Pinefield Radio Music Director and Crosstown Groove Hour host will be onsite!<br>
    Start/Finish/Festival will be on Larkwell St between 9th Ave &amp; 11th Ave<br>
    Net proceeds benefit the Tall Pines Cycling Club dedicated to getting urban youth on bikes; sharing healthy lifestyle and values.<br>
    Special thanks to the Harrowgate Foundation for their ongoing support.
  </p>

  <aside class="schedule">
    <h2>SCHEDULE:</h2>
    <p>Racing starts<br>at 7:00AM<br>Fun ride on the<br>race course at 12PM<br>Expo &amp; Festival<br>10AM – 6PM</p>
  </aside>

  <div class="partners">
    <div class="partner" style="color:#1f3f8f"><span class="mark" style="background:#1f3f8f"></span>Velo Ridge</div>
    <div class="partner" style="color:#c9a227">Copper Square</div>
    <div class="partner" style="color:#111">Trailhead</div>
    <div class="partner" style="color:#b3151d">Tall Pines<br>Cycling Club</div>
    <div class="partner" style="color:#5b2a86"><span class="mark" style="background:#5b2a86"></span>Summit<br>Public TV</div>
    <div class="partner" style="color:#c9a227">Pinefield<br>Radio</div>
    <div class="badge" role="img" aria-label="Partner badge"></div>
    <div class="partner" style="color:#b3151d">Axle Co</div>
  </div>
</div>
</body>
</html>
```